Esthetically Pleasing Core Values and Brand Promise for Accounting Firm

I would like a cohesive design that ties together my core values and brand promise. My firm, Maple Finch Advisory, provides accounting work to small businesses. I prefer modern and clean designs. I want my Core Values and Brand Promise to represent me - sole entrepreneur, married, mother of two kids, modern esthetics, clean lines, organized, colorful (teals, greys, white, yellows)

Industry/Entity Type

Public Accounting

Colors
33b8a4

```html
<!DOCTYPE html>
<html lang="en">
<head>
<meta charset="utf-8">
<title>Maple Finch Advisory – Core Values &amp; Brand Promise</title>
<link href="https://fonts.googleapis.com/css2?family=Montserrat:wght@400;500;600;700&display=swap" rel="stylesheet">
<style>
  :root {
    --teal: #1c9f98;
    --teal-dark: #137d78;
    --ink: #2f2f33;
    --grey: #505055;
    --light-grey: #e4e8ea;
    --white: #ffffff;
    --backdrop-a: #3b3552;
    --backdrop-b: #2c6e72;
    --photo-a: #d9d6d0;
    --photo-b: #9b7a58;
  }
  * { box-sizing: border-box; margin: 0; padding: 0; }
  html, body { width: 1200px; height: 899px; overflow: hidden; }
  body {
    background: var(--light-grey);
    font-family: "Montserrat", sans-serif;
    color: var(--ink);
    position: relative;
  }
  .flyer {
    position: absolute;
    left: 303px; top: 30px;
    width: 594px; height: 840px;
    background: linear-gradient(160deg, #ffffff 60%, #eef1f2 100%);
    overflow: hidden;
    box-shadow: 0 10px 30px rgba(0,0,0,.18);
  }
  .hero { position: absolute; left: 0; top: 0; width: 594px; height: 405px; }

  .brand-name {
    position: absolute; left: 395px; top: 78px; width: 190px;
    text-align: center; color: var(--teal); font-weight: 400;
    line-height: 1;
  }
  .brand-name .line-big { display: block; font-size: 44px; letter-spacing: 2px; }
  .brand-name .line-small { display: block; font-size: 20px; letter-spacing: 3px; margin-top: 8px; }

  .contact { position: absolute; right: 18px; top: 222px; list-style: none; }
  .contact li {
    display: flex; justify-content: flex-end; align-items: center; gap: 8px;
    font-size: 11.5px; color: var(--ink); text-align: right; line-height: 1.35;
    margin-bottom: 10px;
  }
  .contact li.phone { font-size: 14px; font-weight: 700; }
  .contact svg { width: 12px; height: 12px; flex: none; }

  .section-band {
    position: absolute; left: 0; width: 594px; height: 44px;
  }
  .section-band svg { position: absolute; inset: 0; }
  .section-band h2 {
    position: relative; padding-left: 38px; line-height: 44px;
    color: var(--white); font-size: 24px; font-weight: 500; letter-spacing: .5px;
  }
  .section-band h2 strong { font-weight: 700; }
  .band-values { top: 420px; }
  .band-promise { top: 677px; }

  .values {
    position: absolute; left: 14px; top: 484px; width: 566px;
    display: flex;
  }
  .value {
    flex: 1; text-align: center; padding: 0 8px;
    border-left: 2px solid var(--teal);
  }
  .value:first-child { border-left: none; }
  .value .icon { width: 78px; height: 78px; margin: 4px auto 18px; display: block; }
  .value h3 { font-size: 12.5px; font-weight: 700; margin-bottom: 12px; }
  .value:nth-child(odd) h3 { color: var(--teal); }
  .value p { font-size: 10.5px; line-height: 1.3; color: var(--grey); }

  .promises {
    position: absolute; left: 30px; top: 740px; width: 540px;
    display: flex; gap: 0;
  }
  .promise { flex: 1; padding-right: 14px; }
  .promise + .promise { border-left: 1px solid #9a9a9e; padding-left: 18px; padding-right: 0; }
  .promise h3 {
    display: flex; align-items: center; gap: 8px;
    color: var(--teal); font-size: 15px; font-weight: 700; margin-bottom: 12px;
  }
  .promise h3 svg { width: 20px; height: 18px; }
  .promise p { font-size: 10.5px; line-height: 1.35; color: var(--grey); text-align: justify; }

  .footer-strip {
    position: absolute; left: 0; bottom: 0; width: 594px; height: 14px;
    background: linear-gradient(90deg, var(--teal-dark), var(--teal));
  }
</style>
</head>
<body>
<main class="flyer">
  <svg class="hero" viewBox="0 0 594 405" aria-hidden="false">
    <defs>
      <linearGradient id="backdrop-tone" x1="0" y1="0" x2="1" y2="0">
        <stop offset="0" stop-color="var(--backdrop-a)"/>
        <stop offset="1" stop-color="var(--backdrop-b)"/>
      </linearGradient>
      <linearGradient id="photo-tone" x1="0" y1="0" x2="0.6" y2="1">
        <stop offset="0" stop-color="#7f8a8c"/>
        <stop offset="0.45" stop-color="var(--photo-a)"/>
        <stop offset="1" stop-color="var(--photo-b)"/>
      </linearGradient>
    </defs>
    <polygon points="0,0 430,0 380,72 0,72" fill="url(#backdrop-tone)" role="img" aria-label="Dark financial chart backdrop"/>
    <polygon points="0,72 22,72 0,130" fill="var(--teal)"/>
    <polygon points="32,62 338,62 388,162 388,400 0,400 0,136" fill="url(#photo-tone)" role="img" aria-label="Photo of hands typing on a laptop showing a spreadsheet"/>
    <polygon points="594,255 594,400 535,400" fill="var(--teal)"/>
  </svg>

  <div class="brand-name">
    <span class="line-big">MAPLE</span>
    <span class="line-big">FINCH</span>
    <span class="line-small">ADVISORY</span>
  </div>

  <ul class="contact">
    <li>1180 Harbor View Road,<br>Suite 300 Brookvale, CA 90210
      <svg viewBox="0 0 12 12"><path d="M6 1a3.5 3.5 0 0 0-3.5 3.5C2.5 7 6 11 6 11s3.5-4 3.5-6.5A3.5 3.5 0 0 0 6 1z" fill="none" stroke="var(--teal)" stroke-width="1.3"/><circle cx="6" cy="4.5" r="1.2" fill="var(--teal)"/></svg>
    </li>
    <li>www.maplefinchadvisory.com
      <svg viewBox="0 0 12 12"><circle cx="6" cy="6" r="5" fill="none" stroke="var(--teal)" stroke-width="1.2"/><path d="M1 6h10M6 1c-2 2.5-2 7.5 0 10M6 1c2 2.5 2 7.5 0 10" fill="none" stroke="var(--teal)" stroke-width="1"/></svg>
    </li>
    <li class="phone">555-014-2290
      <svg viewBox="0 0 12 12"><path d="M2 4c0-1.5 1.5-2.5 4-2.5S10 2.5 10 4l-2 .5-.5-1.2h-3L4 4.5zM3 10l1-4.5h4L9 10z" fill="var(--teal)"/></svg>
    </li>
  </ul>

  <section class="section-band band-values">
    <svg viewBox="0 0 594 44" aria-hidden="true">
      <polygon points="0,0 300,0 322,44 0,44" fill="var(--teal)"/>
      <polygon points="512,0 594,0 594,44 534,44" fill="var(--teal)"/>
    </svg>
    <h2><strong>CORE</strong> VALUES</h2>
  </section>

  <div class="values">
    <article class="value">
      <svg class="icon" viewBox="0 0 78 78" aria-hidden="true">
        <circle cx="39" cy="39" r="37" fill="none" stroke="var(--teal)" stroke-width="2"/>
        <circle cx="39" cy="39" r="31" fill="var(--teal)"/>
        <rect x="28" y="26" width="22" height="18" rx="5" fill="none" stroke="#fff" stroke-width="2.5"/>
        <path d="M33.5 26v18M39 26v18M44.5 26v18M31 44v10h16V44" fill="none" stroke="#fff" stroke-width="2.5"/>
      </svg>
      <h3>EMPOWER</h3>
      <p>we are dedicated, appreciative and respectful of people's time and purpose.</p>
    </article>
    <article class="value">
      <svg class="icon" viewBox="0 0 78 78" aria-hidden="true">
        <circle cx="39" cy="39" r="37" fill="none" stroke="var(--ink)" stroke-width="2"/>
        <circle cx="39" cy="39" r="31" fill="var(--ink)"/>
        <circle cx="39" cy="39" r="18" fill="none" stroke="#fff" stroke-width="2"/>
        <circle cx="39" cy="30" r="4" fill="#fff"/><circle cx="30" cy="42" r="4" fill="#fff"/>
        <circle cx="48" cy="42" r="4" fill="#fff"/><circle cx="39" cy="45" r="3.5" fill="#fff"/>
      </svg>
      <h3>CLIENT FOCUSED</h3>
      <p>we provide a personal service that goes above the standards of professional care.</p>
    </article>
    <article class="value">
      <svg class="icon" viewBox="0 0 78 78" aria-hidden="true">
        <circle cx="39" cy="39" r="37" fill="none" stroke="var(--teal)" stroke-width="2"/>
        <circle cx="39" cy="39" r="31" fill="var(--teal)"/>
        <path d="M39 22v30M31 53h16M25 28h28M29 28l-5 12M29 28l5 12M49 28l-5 12M49 28l5 12" fill="none" stroke="#fff" stroke-width="2"/>
        <path d="M23 40a6 4 0 0 0 12 0zM43 40a6 4 0 0 0 12 0z" fill="#fff"/>
      </svg>
      <h3>RECTITUDE</h3>
      <p>we know the difference between what we have the right to do and what the right thing to do is.</p>
    </article>
    <article class="value">
      <svg class="icon" viewBox="0 0 78 78" aria-hidden="true">
        <circle cx="39" cy="39" r="37" fill="none" stroke="var(--ink)" stroke-width="2"/>
        <circle cx="39" cy="39" r="31" fill="var(--ink)"/>
        <circle cx="39" cy="39" r="18" fill="none" stroke="#fff" stroke-width="2"/>
        <polygon points="42,26 32,41 38,41 35,52 46,36 40,36" fill="#fff"/>
      </svg>
      <h3>RELENTLESS</h3>
      <p>we believe that the longer we try to do our best, the better we become.</p>
    </article>
  </div>

  <section class="section-band band-promise">
    <svg viewBox="0 0 594 44" aria-hidden="true">
      <polygon points="0,0 300,0 322,44 0,44" fill="var(--teal)"/>
      <polygon points="512,0 594,0 594,44 534,44" fill="var(--teal)"/>
    </svg>
    <h2><strong>BRAND</strong> PROMISE</h2>
  </section>

  <div class="promises">
    <article class="promise">
      <h3><svg viewBox="0 0 20 18" aria-hidden="true"><rect x="1" y="4" width="13" height="13" fill="none" stroke="var(--ink)" stroke-width="1.8"/><path d="M4 10l4 4L19 1" fill="none" stroke="var(--teal)" stroke-width="2.5"/></svg>TAX</h3>
      <p>Maple Finch provides all clients with a trusted tax advisor who provides accuracy in all filings and ensures your compliance with all government agencies.</p>
    </article>
    <article class="promise">
      <h3><svg viewBox="0 0 20 18" aria-hidden="true"><rect x="1" y="4" width="13" height="13" fill="none" stroke="var(--ink)" stroke-width="1.8"/><path d="M4 10l4 4L19 1" fill="none" stroke="var(--teal)" stroke-width="2.5"/></svg>ACCOUNTING</h3>
      <p>Maple Finch provides all business owners with the financial visibility needed to foster growth and facilitate goals.</p>
    </article>
  </div>

  <div class="footer-strip"></div>
</main>
</body>
</html>
```